Zielgruppe
Wir beraten Menschen aus unterschiedlichen Branchen, die im Rahmen Ihrer Tätigkeit vor einem technologischen Problem bzw. einer technologischen Lücke stehen und helfen diesen über vielfältige Bausteine, um so dem Unternehmen ein Unternehmensupgrade zu verschaffen. Wir schlagen somit eine Brücke zwischen dem Stand von heute in einem Unternehmen zu einem besseren Stand morgen.
Konkret betreiben wir unter anderem externes Projektmanagement, beschaffen Informationen unterschiedlicher Art, vermitteln Kooperationspartner, beraten individuell uvm.
Ob jemand nach einer neuen, innovativen Technologie sucht, Partner benötigt, um eigene Neuentwicklungen voranzutreiben, ein neues Produkt fürs eigene Unternehmen und einen entsprechenden Prototypen sucht, verwendete Stoffe mit anderen ersetzen will - mithilfe unseres weltweiten Expertennetzwerks von über 600.000 direkten Ansprechpartnern finden wir für die meisten Nöte dieser Art eine Lösung bzw. jemanden, der diese lösen kann.
Im Grunde genommen beseitigen wir Engpässe innerhalb von Industrieunternehmen, die beispielsweise sein können
-fehlende TEchnologien/Ersatzprodukte/Ersatzstoffe
-fehlende Ideen für Neuentwicklungen
-fehlendes Wissen im Unternehmen
-fehlende Objektivität hinsichtlich interner Verbesserungsmöglichkeiten
-fehlende Zeit für eigene Projekte, Neuentwicklungen und Suchen versch. Art
Wir finden
- neue Technologien, Ersatzprodukte, Ersatzstoffe
- Ideen für Neuentwicklungen und zusätzlich diejenigen, die dabei unterstützen können
- neue Märkte, um das Unternehmen zu erweitern
- das fehlende Wissen
- den nötigen Abstand, um interne Prozesse und Abläufe objektiv zu beurteilen und geben Vorschläge zur Veränderung/Verbesserung
- passende Realisierungspartner
Wie?
- wir recherchieren (Patente, Literatur) und sammeln Hintergrundwissen
- wir befragen unser Netzwerk und Unternehmen/Wissenschaftler
- wir setzen unsere Töchter..
Aufgabenstellung
Wir benötigen einen faltbaren Flyer, allerdings keinen klassischen, sondern wie ein Theatervorhang. Beispielbilder sind anbei (wir würden die Flyer drucken lassen und dann selbst falten). Wir gehen gerne andere Wege, auch in unseren Projekten.
Der Mensch und dessen Wünsche soll im Mittelpunkt stehen.
Design sollte nicht zu verspielt sein, sich daran orientieren, dass deutsche Unternehmen damit angesprochen werden.
Einen Beispielflyer mit den (noch variablen) Texten ist beigefügt, das Design muss sich nicht daran orientieren. Gute Alternativen sind mehr als gewünscht.
Der Gedanke hinter dem Flyer: Wir schlagen eine Brücke für den Kunden/Menschen zu seinem Ziel. Die Tools, die wir dazu nutzen sind Steine oder wir sprengen den Weg frei zum Ziel o.ä. Auch hier sind Alternativen mehr als willkommen.
Sie dürfen sich so weit wie möglich vom Beispielentwurf und dem Bild der Brücke zum Ziel lösen. Je kreativer und einleuchtender, desto besser. Gerne auch humorvoll, gerne einfach anders.

```html
<!DOCTYPE html>
<html lang="de">
<head>
<meta charset="utf-8">
<title>ntb Flyer – Vorhangfalz</title>
<link rel="stylesheet" href="https://fonts.googleapis.com/css2?family=Lato:ital,wght@0,300;0,400;0,700;0,900;1,700&display=swap">
<style>
:root{
  --bg:#e3e5e9;
  --blue:#2f3c8c;
  --blue-text:#2d3a86;
  --grey-text:#5c606b;
  --white:#ffffff;
  --fold:#d6d6d6;
}
*{box-sizing:border-box;margin:0;padding:0}
html,body{width:1200px;height:1200px;overflow:hidden;background:var(--bg);font-family:'Lato',sans-serif;color:var(--blue-text)}
.sheet{position:absolute;left:205px;width:776px;background:linear-gradient(180deg,#f2f2f2,#e6e6e6);box-shadow:0 2px 6px rgba(0,0,0,.18)}
.sheet-outer{top:28px;height:552px}
.sheet-inner{top:612px;height:546px}
.fold{position:absolute;top:0;bottom:0;width:1px;background:var(--fold)}
.abs{position:absolute}
.photo-cliff{position:absolute;top:0;bottom:0;background:linear-gradient(180deg,#9a5a24 0%,#c27a3a 18%,#8fb1d0 38%,#a9c4dc 55%,#4d7fa6 70%,#c59a3a 82%,#d8a83c 100%)}
.photo-cliff.right{background:linear-gradient(180deg,#8a4d1f 0%,#b9722f 20%,#7fa4c6 40%,#c99a3b 65%,#e0b245 80%,#c9972f 100%)}
.blue-box{position:absolute;background:var(--blue);color:var(--white)}
b,strong{font-weight:700}
.brand{position:absolute;display:flex;align-items:center;gap:6px;font-weight:700;font-size:22px;color:var(--blue)}
.brand .dot{width:20px;height:20px;border-radius:50%;background:var(--blue)}
.headline{font-weight:300;font-size:17px;line-height:1.25;white-space:nowrap}
.headline.tight{font-size:16px;line-height:1.3}
.team-photo{position:absolute;background:linear-gradient(135deg,#d9d3cc 0%,#b8a99a 40%,#4a5470 75%,#2e3447 100%)}
.contact{position:absolute;font-size:8.6px;line-height:1.35;color:var(--grey-text);font-weight:300;white-space:nowrap}
.contact .name{color:var(--blue-text);font-weight:700}
.contact svg{width:8px;height:8px;vertical-align:-1px;margin-right:5px;fill:var(--blue-text)}
.benefits{list-style:none;font-size:8.8px;line-height:1.28;font-weight:300;white-space:nowrap}
.benefits li{position:relative;padding-left:21px;margin-bottom:8px}
.benefits li svg{position:absolute;left:6px;top:2px;width:8px;height:8px}
.band{position:absolute;left:0;right:0;top:85px;height:77px;background:var(--blue);color:var(--white)}
.band p{position:absolute;left:235px;top:7px;font-size:17px;line-height:1.25;font-weight:300;white-space:nowrap}
.quote{position:absolute;background:var(--blue);color:var(--white);font-weight:700;font-size:17px;padding:1px 7px;line-height:1.3;white-space:nowrap}
.tool{position:absolute;font-size:8.6px;line-height:1.3;color:var(--grey-text);font-weight:300;white-space:nowrap}
.tool b{color:var(--blue-text)}
.tool-icon{position:absolute;width:16px;height:16px}
.divider{position:absolute;width:1px;background:var(--blue);top:195px;height:225px}
.rocket-art{position:absolute;background:linear-gradient(180deg,#c9cbd6,#b3b7c9)}
</style>
</head>
<body>

<section class="sheet sheet-outer">
  <div class="photo-cliff" style="left:0;width:193px" role="img" aria-label="Kletterer unter einem Felsüberhang über dem Meer"></div>
  <div class="blue-box" style="left:35px;top:333px;width:141px;height:219px;padding:26px 0 0 12px">
    <p class="headline tight">Wir beseitigen<br>Ihre <b>Engpässe</b><br>und sind Ihnen<br>ein strategischer<br><b>Partner</b> von<br>Beginn bis zum<br>Ende Ihres<br>Projekts.</p>
  </div>

  <div class="fold" style="left:193px"></div>
  <div class="brand" style="left:447px;top:30px"><span class="dot"></span>ntb</div>
  <p class="headline abs" style="left:243px;top:189px">Sie nennen mir Ihre Ziele und Wünsche.<br>Gemeinsam definieren wir Ihr Projekt.</p>
  <div class="team-photo" style="left:245px;top:243px;width:292px;height:153px" role="img" aria-label="Team schaut gemeinsam auf einen Bildschirm"></div>
  <p class="headline abs" style="left:245px;top:411px">Nutzen Sie unser Expertennetzwerk.</p>
  <div class="contact" style="left:243px;top:449px">
    <div class="name">Dr. Lena Vossberg</div>
    <div>Geschäftsführende Gesellschafterin</div>
    <div class="name" style="margin-top:6px">Nordhöfer Technikberatung GmbH</div>
    <div><svg viewBox="0 0 10 10"><path d="M1 1h1v8H1zM2 1h7l-2 2 2 2H2z"/></svg>Lindenhofweg 14</div>
    <div><svg viewBox="0 0 10 10"><path d="M5 1 0 5h1.5v4h2.5V6h2v3h2.5V5H10z"/></svg>86152 Talheim</div>
  </div>
  <div class="contact" style="right:240px;top:476px;text-align:right">
    <div><svg viewBox="0 0 10 10"><path d="M1 3c2-2 6-2 8 0v2H7V4H3v1H1zM2 6h6l1 3H1z"/></svg>+49 821 400 27 90</div>
    <div><svg viewBox="0 0 10 10"><path d="M0 2h10v6H0zM1 3v.5l4 2.5 4-2.5V3z"/></svg>vossberg@ntberatung.de</div>
    <div><svg viewBox="0 0 10 10"><circle cx="5" cy="5" r="4.5"/></svg>www.ntberatung.de</div>
  </div>

  <div class="fold" style="left:583px"></div>
  <div class="photo-cliff right" style="left:583px;width:193px" role="img" aria-label="Kletterer an sonnigen Felsen über dem Meer"></div>
  <div class="blue-box" style="left:600px;top:0;width:141px;height:387px;padding:16px 0 0 11px">
    <p class="headline">Sie stehen<br>vor einem<br>technologischen<br>Problem?</p>
    <p style="font-weight:900;font-size:17px;margin-top:9px">Keine Sorge.</p>
    <p style="font-size:8.8px;font-weight:300;margin:4px 0 11px"><b><i>ntb</i></b> bietet mir:</p>
    <ul class="benefits">
      <li><svg viewBox="0 0 10 10"><path d="M1 5l3 3 5-6" stroke="#fff" stroke-width="2" fill="none"/></svg>...neue Technologien,<br>Ersatzprodukte/<br>Ersatzstoffe</li>
      <li><svg viewBox="0 0 10 10"><path d="M1 5l3 3 5-6" stroke="#fff" stroke-width="2" fill="none"/></svg>...Ideen für<br>Neuentwicklungen</li>
      <li><svg viewBox="0 0 10 10"><path d="M1 5l3 3 5-6" stroke="#fff" stroke-width="2" fill="none"/></svg>...Zugang zu neuen<br>Märkten</li>
      <li><svg viewBox="0 0 10 10"><path d="M1 5l3 3 5-6" stroke="#fff" stroke-width="2" fill="none"/></svg>...ergänzendes Wissen</li>
      <li><svg viewBox="0 0 10 10"><path d="M1 5l3 3 5-6" stroke="#fff" stroke-width="2" fill="none"/></svg>...interne Prozess- und<br>Ablaufverbesserungen</li>
      <li><svg viewBox="0 0 10 10"><path d="M1 5l3 3 5-6" stroke="#fff" stroke-width="2" fill="none"/></svg>...passende Partner<br>zur Realisierung</li>
      <li><svg viewBox="0 0 10 10"><path d="M1 5l3 3 5-6" stroke="#fff" stroke-width="2" fill="none"/></svg>...ein Expertennetzwerk<br>von über 600.000<br>Ansprechpartnern</li>
    </ul>
  </div>
</section>

<section class="sheet sheet-inner">
  <div class="fold" style="left:194px"></div>
  <div class="fold" style="left:581px"></div>
  <div class="brand" style="left:672px;top:22px"><span class="dot"></span>ntb</div>

  <div class="band">
    <p><b><i>ntb</i></b> übernimmt die <b>Gesamtprojektleitung</b><br>als Generalunternehmer und nutzt für Ihr<br>Projekt eigene, passende Tools:</p>
  </div>

  <p class="headline abs" style="left:15px;top:188px">Sie stecken im Projekt<br>fest und kommen nicht<br>weiter? Wir helfen<br>Ihnen <b>schnell</b>, einfach<br>und <b>unkompliziert</b>.</p>
  <span class="quote" style="left:17px;top:330px">“Geht nicht,</span>
  <span class="quote" style="left:73px;top:352px">gibt´s nicht.”</span>

  <div class="divider" style="left:266px"></div>
  <div class="divider" style="left:428px"></div>

  <svg class="tool-icon" style="left:236px;top:196px" viewBox="0 0 16 16" fill="#555"><circle cx="8" cy="4" r="3"/><circle cx="3" cy="10" r="2"/><circle cx="13" cy="10" r="2"/><rect x="5" y="9" width="6" height="6" rx="2"/></svg>
  <p class="tool" style="left:273px;top:195px">Heterogenes Team mit<br><b>kreativen Köpfen</b></p>
  <svg class="tool-icon" style="left:400px;top:196px" viewBox="0 0 16 16" fill="none" stroke="#555" stroke-width="1.4"><rect x="1" y="2" width="14" height="12"/><path d="M4 6h2M8 6h2M12 6h1M4 10h2M8 10h2M12 10h1"/></svg>
  <p class="tool" style="left:437px;top:195px"><b>Patent- und<br>Literatur</b>recherchen</p>

  <svg class="tool-icon" style="left:236px;top:242px" viewBox="0 0 16 16" fill="none" stroke="#555" stroke-width="1.4"><rect x="3" y="1" width="10" height="14"/><path d="M5 5h6M5 8h6M5 11h6"/></svg>
  <p class="tool" style="left:273px;top:235px">Tochterunternehmen für<br>Spezialthemen;<br><b>Firmenlotse,<br>Trio3, q-plan</b></p>
  <svg class="tool-icon" style="left:400px;top:242px" viewBox="0 0 16 16" fill="none" stroke="#555" stroke-width="1.4"><rect x="1" y="2" width="14" height="9"/><path d="M8 11v4M5 15h6M4 8l3-3 2 2 3-3"/></svg>
  <p class="tool" style="left:437px;top:235px">Geographisch spezifische<br>Projektausschreibungen<br>und <b>Netzwerkbefragungen</b></p>

  <svg class="tool-icon" style="left:236px;top:303px" viewBox="0 0 16 16" fill="none" stroke="#555" stroke-width="1.4"><circle cx="8" cy="8" r="6.5"/><path d="M1.5 8h13M8 1.5c-3 3-3 10 0 13M8 1.5c3 3 3 10 0 13"/></svg>
  <p class="tool" style="left:273px;top:301px"><b>Globales Netzwerk</b> in jedem<br>Technologiebereich</p>
  <svg class="tool-icon" style="left:400px;top:301px" viewBox="0 0 16 16" fill="none" stroke="#555" stroke-width="1.4"><circle cx="8" cy="6.5" r="5"/><path d="M6 13h4M6.5 15h3"/></svg>
  <p class="tool" style="left:437px;top:301px">Individuelles<br><b>Projektmanagement</b></p>

  <svg class="tool-icon" style="left:236px;top:351px" viewBox="0 0 16 16" fill="none" stroke="#555" stroke-width="1.4"><path d="M3 1h7l3 3v11H3z"/><circle cx="8" cy="9" r="2.5"/></svg>
  <p class="tool" style="left:274px;top:349px">Demonstrator- und<br><b>Prototypenbau</b></p>
  <svg class="tool-icon" style="left:400px;top:351px" viewBox="0 0 16 16" fill="none" stroke="#555" stroke-width="1.4"><rect x="3" y="2" width="10" height="13"/><path d="M5 7l2 2 4-4M5 12h6"/></svg>
  <p class="tool" style="left:438px;top:349px">Tests, Sprint,<br><b>Validierung</b></p>

  <svg class="tool-icon" style="left:236px;top:396px" viewBox="0 0 16 16" fill="none" stroke="#555" stroke-width="1.4"><rect x="1" y="1" width="6" height="5"/><rect x="9" y="10" width="6" height="5"/><path d="M4 6v6h5M10 4h3v4"/></svg>
  <p class="tool" style="left:274px;top:393px">Dokumentation und<br><b>Visualisierung</b> über<br>Web-Plattform NOVA</p>
  <svg class="tool-icon" style="left:400px;top:398px" viewBox="0 0 16 16" fill="none" stroke="#555" stroke-width="1.4"><rect x="2" y="1" width="12" height="14"/><path d="M5 11v2M8 9v4M11 7v6M5 4h6"/></svg>
  <p class="tool" style="left:438px;top:400px">Professionelle <b>Marktanalyse</b><br>und Technologieauswertung</p>

  <svg class="abs" style="left:0;top:478px" width="250" height="12" viewBox="0 0 250 12"><path d="M0 8 L240 5.5" stroke="#2f3c8c" stroke-width="1"/><path d="M240 1.5 L248 5.5 L240 9.5z" fill="#2f3c8c"/></svg>
  <p class="headline abs" style="left:273px;top:462px"><b>Unternehmensupgrade</b> durch<br>technologische Beratung</p>

  <p class="headline abs" style="left:597px;top:188px">Wir <b>lösen</b> Ihre<br>unternehmerischen<br><b>Probleme</b> durch unser<br>Wissen und unsere<br>Tools.</p>
  <div class="rocket-art" style="left:627px;top:306px;width:105px;height:113px;border-radius:4px" role="img" aria-label="Illustration: große Rakete zwischen zwei kleinen Raketen"></div>
</section>

</body>
</html>
```